Design for an exciting fantasy football leaderboard

We are looking for an exciting design for our fantasy football weekly rankings (a leaderboard for player stats & values.) Each day our intelligence engine runs and generates new values for ZPA players. The players are then ranked from 1 (best) to something greater (say 40 or 50 players) by a particular position. Our users log in to see the list to help understand player values for their add/drops and to help set their lineups.

Here is an example of the existing page: http://www.pelwick-hub.example/fantasy-football-rankings/weekly-rankings/qb/

Items that we might like to see:
- Our player value (score from 100 HIGH to 1 LOW) worked in
- Some "glory" stats - rushing yards, rushing TDs, opportunities (for RBs as an example) worked into the table
- A better way to share statistical movement of the players value
- A way to use icons (and some icons) to show special player call outs
- Improved UI for the buttons to navigate to other positions and scoring systems
- A design call out that highlights that each player name can be clicked to go to the player page
- A small call out box that describes that our engine is working and why it is cool
- A date last processed that is not overwhelming but noticeable
- A sense of energy and movement. This should be a fun and exciting view

Feel free to email with questions or thoughts

What we'd like is a more exciting format that uses icons and imagery to denote players who are rising, falling, hot, cold, injured, etc.

This is our test run of Pixel Forum. We have a lot of similar projects that we would like to work on in 2014. Each year our off-season begins on JAN 1 - so we are excited to begin working. If we can find a designer or two that understands the visual energy of fantasy football and can pickup our brand from the existing site - we'll have more work.
Updates

We've updated the project to be payment guaranteed.  We hope that will show that we are serious about working with Pixel Forum designers in 2014 on a variety of projects.

I'd like to thank everyone who participated in the contest.  It was a pleasure to work with all of you and I thank you for taking the time to work on our project.   I am confident that we will see you again in the future with additional contests!

Target Market(s)

We are building a new brand around fantasy football analytics - our audience cares greatly about getting detailed analysis for their fantasy football teams. The look should be professional in appearance (nothing cartoony) and be easy to read. Our audience is primarily male...educated beyond high school.

Check out our site as it is today: http://www.pelwick-hub.example. Our preseason designs are stronger than the weekly rankings. For instance, we all liked the design of this page: http://www.pelwick-hub.example/2013-fantasy-football-rankings/projections/rb/

Industry/Entity Type

Call

Requirements
Must have
• - Improved UX for the page and the sub navigation
- Must fit and work well on tablets and normal PCs
- Rankings should be easy to read and well laid out
- Clean, professional design
Nice to have
• - Sense of movement and momentum...these players are moving up and down daily and that is important to our users
- Icons for Rising, Falling, Sleeper, Suggested Waiver claim, Hot, Cold, etc
- Sense of excitement...avoid the wall of words
- Possibly a cool "light box" window that gives more info about the player if someone rolls over the name, or taps a "more info" icon. If someone clicks the "go to player page" in the light box then they would surf to the player page.
Should not have
• - Cliché football icons or pictures of turf fields
- Comic sans font
- Soccer imagery - this is ZPA American Football

```html
<!DOCTYPE html>
<html lang="en">
<head>
<meta charset="utf-8">
<title>QB Weekly Rankings</title>
<link rel="stylesheet" href="https://fonts.googleapis.com/css2?family=Open+Sans:wght@400;600;700&display=swap">
<style>
:root{
  --bg:#1a1b1e;
  --panel-top:#2e2f33;
  --panel-bottom:#1f2023;
  --panel-edge:#55575c;
  --band-stats:#3e4044;
  --cell-white:#ffffff;
  --cell-grey:#ebecee;
  --text-dark:#4a4a4a;
  --text-muted:#a8a9ac;
  --label-light:#ffffff;
  --rank-green:#7ec16a;
  --qb-grey:#c9c9c9;
  --hot:#f0644a;
  --up:#7ec16a;
  --down:#e8503a;
  --bar-track:#e6e6e6;
  --bar-start:#7ccf4a;
  --bar-end:#ffde17;
  --head-1:#c4a67b;
  --head-2:#173b5b;
  --head-3:#0c2b5c;
  --head-4:#2c4a3f;
  --head-5:#0898c9;
  --avatar-top:#d9d9d9;
  --avatar-bottom:#b7b7b7;
}
*{box-sizing:border-box;margin:0;padding:0}
html,body{width:1200px;height:683px;overflow:hidden;background:var(--bg);font-family:'Open Sans',Arial,sans-serif}
.rankings{
  position:absolute;left:15px;top:35px;width:1170px;height:612px;
  background:linear-gradient(135deg,var(--panel-top),var(--panel-bottom));
  border:2px solid var(--panel-edge);
}
.player-row{position:absolute;left:19px;width:1131px;height:92px}
.player-row:nth-child(1){top:20px;--head:var(--head-1)}
.player-row:nth-child(2){top:137px;--head:var(--head-2)}
.player-row:nth-child(3){top:254px;--head:var(--head-3)}
.player-row:nth-child(4){top:371px;--head:var(--head-4)}
.player-row:nth-child(5){top:488px;--head:var(--head-5)}
.row-head{position:absolute;left:0;top:0;width:100%;height:24px;background:var(--head);border-radius:4px 4px 0 0}
.row-main{position:absolute;left:0;top:24px;width:100%;height:38px;background:var(--cell-white)}
.row-stats{position:absolute;left:0;top:62px;width:100%;height:30px;background:var(--band-stats)}
.col-label{position:absolute;top:5px;font-size:11.5px;color:var(--label-light)}
.rank-badge{position:absolute;left:0;top:26px;width:43px;height:42px;background:var(--rank-green);color:#fff;
  font-size:27px;font-weight:600;display:flex;align-items:center;justify-content:center;border-radius:0 4px 4px 0;z-index:2}
.avatar{position:absolute;left:55px;top:1px;width:84px;height:84px;border-radius:50%;border:3px solid #fff;
  background:linear-gradient(180deg,var(--avatar-top),var(--avatar-bottom));z-index:2}
.pos-badge{position:absolute;left:175px;top:7px;width:24px;height:24px;border-radius:50%;background:#f2f2f2;
  color:var(--qb-grey);font-size:10.5px;font-weight:600;display:flex;align-items:center;justify-content:center}
.player-name{position:absolute;left:240px;top:6px;font-size:19.5px;font-weight:600;color:var(--text-dark);white-space:nowrap}
.team-cell{position:absolute;left:496px;top:0;width:156px;height:38px;background:var(--cell-grey);
  font-size:19.5px;font-weight:600;color:var(--text-dark);padding:6px 0 0 9px;white-space:nowrap}
.status-icons{position:absolute;left:688px;top:10px;display:flex;gap:26px}
.move-cell{position:absolute;left:837px;top:0;width:103px;height:38px;background:var(--cell-grey);
  color:var(--text-dark);display:flex;align-items:center;padding-left:17px;gap:5px}
.move-num{font-size:19px;font-weight:600}
.move-unit{font-size:11.5px;font-weight:600;margin-top:4px}
.value-num{position:absolute;left:964px;top:6px;font-size:19px;font-weight:600;color:var(--text-dark)}
.value-bar{position:absolute;left:996px;top:12px;width:113px;height:15px;border-radius:8px;background:var(--bar-track);overflow:hidden}
.value-fill{display:block;height:100%;border-radius:8px;background:linear-gradient(90deg,var(--bar-start),var(--bar-end))}
.stat{position:absolute;top:7px;font-size:12px;color:var(--text-muted);white-space:nowrap}
.stat b{color:#fff;font-weight:700;margin-left:6px}
</style>
</head>
<body>
<svg width="0" height="0" style="position:absolute">
  <defs>
    <symbol id="icon-hot" viewBox="0 0 14 18"><path d="M7 0C8 4 13 6 13 11.5A6 6 0 0 1 1 11.5C1 8 3.5 6.5 4 4c1.5 1.5 1.5 3.5 1.5 4.5C7.5 7 8 4 7 0zM7 9c-.5 2-2.5 2.8-2.5 5a2.5 2.5 0 0 0 5 0C9.5 12 7.5 11 7 9z" fill="#f0644a" fill-rule="evenodd"/></symbol>
    <symbol id="icon-rising" viewBox="0 0 18 18"><path d="M9 1 17 10H1z" fill="#f0644a"/><rect x="1" y="12" width="16" height="1.6" fill="#f0644a"/><rect x="1" y="15.4" width="16" height="1.6" fill="#f0644a"/></symbol>
    <symbol id="arrow-up" viewBox="0 0 14 16"><path d="M7 0 14 7H9.5v9h-5V7H0z" fill="#7ec16a"/></symbol>
    <symbol id="arrow-down" viewBox="0 0 14 16"><path d="M7 16 0 9h4.5V0h5v9H14z" fill="#e8503a"/></symbol>
  </defs>
</svg>

<main class="rankings">
  <section class="player-row">
    <div class="row-head">
      <span class="col-label" style="left:7px">Rank</span><span class="col-label" style="left:165px">Position</span><span class="col-label" style="left:240px">Player</span><span class="col-label" style="left:496px">Team</span><span class="col-label" style="left:685px">Status</span><span class="col-label" style="left:846px">Movement</span><span class="col-label" style="left:958px">Value</span>
    </div>
    <div class="row-main">
      <span class="pos-badge">QB</span><span class="player-name">Marcus Ellery</span><span class="team-cell">Harbormen</span>
      <span class="status-icons"><svg width="14" height="18"><use href="#icon-hot"/></svg><svg width="18" height="18"><use href="#icon-rising"/></svg></span>
      <span class="move-cell"><span class="move-num">5</span><span class="move-unit">places</span><svg width="14" height="16"><use href="#arrow-up"/></svg></span>
      <span class="value-num">98</span><span class="value-bar"><span class="value-fill" style="width:90%"></span></span>
    </div>
    <div class="row-stats">
      <span class="stat" style="left:172px">Stats:</span><span class="stat" style="left:218px">RY<b>150</b></span><span class="stat" style="left:289px">RTD<b>4</b></span><span class="stat" style="left:355px">LG<b>39</b></span><span class="stat" style="left:506px">Ts:<b>2nd Overall</b></span>
    </div>
    <span class="rank-badge">1</span>
    <span class="avatar" role="img" aria-label="Player headshot photo"></span>
  </section>

  <section class="player-row">
    <div class="row-head">
      <span class="col-label" style="left:7px">Rank</span><span class="col-label" style="left:165px">Position</span><span class="col-label" style="left:240px">Player</span><span class="col-label" style="left:496px">Team</span><span class="col-label" style="left:685px">Status</span><span class="col-label" style="left:846px">Movement</span><span class="col-label" style="left:958px">Value</span>
    </div>
    <div class="row-main">
      <span class="pos-badge">QB</span><span class="player-name">Jonah Whitcombe</span><span class="team-cell">Comets</span>
      <span class="status-icons"><svg width="14" height="18"><use href="#icon-hot"/></svg><svg width="18" height="18"><use href="#icon-rising"/></svg></span>
      <span class="move-cell"><span class="move-num">1</span><span class="move-unit">place</span><svg width="14" height="16"><use href="#arrow-down"/></svg></span>
      <span class="value-num">95</span><span class="value-bar"><span class="value-fill" style="width:86%"></span></span>
    </div>
    <div class="row-stats">
      <span class="stat" style="left:172px">Stats:</span><span class="stat" style="left:218px">RY<b>119</b></span><span class="stat" style="left:289px">RTD<b>4</b></span><span class="stat" style="left:355px">LG<b>17</b></span><span class="stat" style="left:506px">Ts:<b>1st Overall</b></span>
    </div>
    <span class="rank-badge">2</span>
    <span class="avatar" role="img" aria-label="Player headshot photo"></span>
  </section>

  <section class="player-row">
    <div class="row-head">
      <span class="col-label" style="left:7px">Rank</span><span class="col-label" style="left:165px">Position</span><span class="col-label" style="left:240px">Player</span><span class="col-label" style="left:496px">Team</span><span class="col-label" style="left:685px">Status</span><span class="col-label" style="left:846px">Movement</span><span class="col-label" style="left:958px">Value</span>
    </div>
    <div class="row-main">
      <span class="pos-badge">QB</span><span class="player-name">Victor Stroud</span><span class="team-cell">Ironclads</span>
      <span class="status-icons"><svg width="14" height="18"><use href="#icon-hot"/></svg><svg width="18" height="18"><use href="#icon-rising"/></svg></span>
      <span class="move-cell"><span class="move-num">1</span><span class="move-unit">place</span><svg width="14" height="16"><use href="#arrow-down"/></svg></span>
      <span class="value-num">92</span><span class="value-bar"><span class="value-fill" style="width:84%"></span></span>
    </div>
    <div class="row-stats">
      <span class="stat" style="left:172px">Stats:</span><span class="stat" style="left:218px">RY<b>98</b></span><span class="stat" style="left:289px">RTD<b>3</b></span><span class="stat" style="left:355px">LG<b>15</b></span><span class="stat" style="left:506px">Ts:<b>4st Overall</b></span>
    </div>
    <span class="rank-badge">3</span>
    <span class="avatar" role="img" aria-label="Player headshot photo"></span>
  </section>

  <section class="player-row">
    <div class="row-head">
      <span class="col-label" style="left:7px">Rank</span><span class="col-label" style="left:165px">Position</span><span class="col-label" style="left:240px">Player</span><span class="col-label" style="left:496px">Team</span><span class="col-label" style="left:685px">Status</span><span class="col-label" style="left:846px">Movement</span><span class="col-label" style="left:958px">Value</span>
    </div>
    <div class="row-main">
      <span class="pos-badge">QB</span><span class="player-name">Elliot Kasper</span><span class="team-cell">Ironclads</span>
      <span class="status-icons"><svg width="14" height="18"><use href="#icon-hot"/></svg><svg width="18" height="18"><use href="#icon-rising"/></svg></span>
      <span class="move-cell"><span class="move-num">3</span><span class="move-unit">places</span><svg width="14" height="16"><use href="#arrow-up"/></svg></span>
      <span class="value-num">89</span><span class="value-bar"><span class="value-fill" style="width:78%"></span></span>
    </div>
    <div class="row-stats">
      <span class="stat" style="left:172px">Stats:</span><span class="stat" style="left:218px">RY<b>92</b></span><span class="stat" style="left:289px">RTD<b>3</b></span><span class="stat" style="left:355px">LG<b>11</b></span><span class="stat" style="left:506px">Ts:<b>5th Overall</b></span>
    </div>
    <span class="rank-badge">4</span>
    <span class="avatar" role="img" aria-label="Player headshot photo"></span>
  </section>

  <section class="player-row">
    <div class="row-head">
      <span class="col-label" style="left:7px">Rank</span><span class="col-label" style="left:165px">Position</span><span class="col-label" style="left:240px">Player</span><span class="col-label" style="left:496px">Team</span><span class="col-label" style="left:685px">Status</span><span class="col-label" style="left:846px">Movement</span><span class="col-label" style="left:958px">Value</span>
    </div>
    <div class="row-main">
      <span class="pos-badge">QB</span><span class="player-name">Rafael Dunmore</span><span class="team-cell">Ironclads</span>
      <span class="status-icons"><svg width="14" height="18"><use href="#icon-hot"/></svg><svg width="18" height="18"><use href="#icon-rising"/></svg></span>
      <span class="move-cell"><span class="move-num">1</span><span class="move-unit">place</span><svg width="14" height="16"><use href="#arrow-up"/></svg></span>
      <span class="value-num">88</span><span class="value-bar"><span class="value-fill" style="width:77%"></span></span>
    </div>
    <div class="row-stats">
      <span class="stat" style="left:172px">Stats:</span><span class="stat" style="left:218px">RY<b>85</b></span><span class="stat" style="left:289px">RTD<b>3</b></span><span class="stat" style="left:355px">LG<b>12</b></span><span class="stat" style="left:506px">Ts:<b>8th Overall</b></span>
    </div>
    <span class="rank-badge">5</span>
    <span class="avatar" role="img" aria-label="Player headshot photo"></span>
  </section>
</main>
</body>
</html>
```